Copper wren builds

Copper wren builds is a small construction company.
Who is a licenced builder, Carpenter, joiner,
working on heritage ,new build, speacial projects and sometimes furniture

Industry/Entity Type

Construction

```html
<!DOCTYPE html>
<html lang="en">
<head>
<meta charset="utf-8">
<title>Copper wren builds – Business Card</title>
<link rel="stylesheet" href="https://fonts.googleapis.com/css2?family=Quicksand:wght@500;600&family=Open+Sans:wght@400;600&display=swap">
<style>
  :root {
    --stage: #ecebe8;
    --card: #ffffff;
    --ink: #1c1c1c;
    --ink-soft: #3a3a3a;
    --green: #7dc242;
    --shadow: rgba(0, 0, 0, 0.18);
  }
  * { box-sizing: border-box; margin: 0; padding: 0; }
  html, body {
    width: 1200px; height: 880px; overflow: hidden;
    background: var(--stage);
  }
  .canvas {
    position: relative; width: 1200px; height: 880px;
    display: flex; flex-direction: column; align-items: center; justify-content: center;
    gap: 48px;
  }
  .card {
    position: relative; width: 660px; height: 376px;
    background: var(--card); border-radius: 26px;
    box-shadow: 0 12px 30px var(--shadow);
    overflow: hidden;
  }
  .wordmark {
    display: flex; align-items: center; gap: 12px;
    font-family: "Quicksand", sans-serif; font-weight: 600;
    color: var(--ink); white-space: nowrap;
  }
  .wordmark__dot { border-radius: 50%; background: var(--green); flex: none; }

  /* front */
  .card--front { display: flex; align-items: center; justify-content: center; }
  .card--front .wordmark { font-size: 38px; }
  .card--front .wordmark__dot { width: 30px; height: 30px; }

  /* back */
  .card--back .wordmark {
    position: absolute; right: 44px; top: 62px; font-size: 28px;
  }
  .card--back .wordmark__dot { width: 22px; height: 22px; }
  .holder {
    position: absolute; left: 44px; top: 160px;
    font-family: "Quicksand", sans-serif;
  }
  .holder__name { font-size: 24px; font-weight: 600; color: var(--ink); line-height: 1.2; }
  .holder__name span { color: var(--green); }
  .holder__title { font-size: 15px; font-weight: 500; color: var(--ink-soft); margin-top: 2px; }
  .rule {
    position: absolute; left: 44px; right: 44px; top: 266px;
    height: 2px; background: var(--green);
  }
  .contacts {
    position: absolute; left: 44px; right: 44px; top: 288px;
    display: flex; align-items: center; justify-content: space-between;
    font-family: "Open Sans", sans-serif; font-size: 13px; color: var(--ink);
    white-space: nowrap;
  }
  .contact { display: flex; align-items: center; gap: 7px; }
  .contact svg { width: 20px; height: 20px; flex: none; }
  .divider { width: 1.5px; height: 20px; background: var(--green); flex: none; }
</style>
</head>
<body>
<main class="canvas">
  <section class="card card--front" aria-label="Card front">
    <div class="wordmark"><span class="wordmark__dot"></span>Copper wren builds</div>
  </section>

  <section class="card card--back" aria-label="Card back">
    <div class="wordmark"><span class="wordmark__dot"></span>Copper wren builds</div>

    <div class="holder">
      <p class="holder__name">Marcus <span>Hale</span></p>
      <p class="holder__title">President</p>
    </div>

    <div class="rule"></div>

    <div class="contacts">
      <p class="contact">
        <svg viewBox="0 0 22 22" aria-hidden="true">
          <circle cx="11" cy="11" r="10" fill="none" stroke="var(--green)" stroke-width="1.5"/>
          <rect x="7.5" y="5.5" width="7" height="11" rx="1.2" fill="none" stroke="var(--green)" stroke-width="1.4"/>
          <circle cx="11" cy="14.3" r="0.8" fill="var(--green)"/>
        </svg>
        0431552907
      </p>
      <span class="divider"></span>
      <p class="contact">
        <svg viewBox="0 0 22 22" aria-hidden="true">
          <circle cx="11" cy="11" r="10" fill="none" stroke="var(--green)" stroke-width="1.5"/>
          <rect x="6" y="7.5" width="10" height="7" rx="1" fill="none" stroke="var(--green)" stroke-width="1.4"/>
          <path d="M6 7.8 L11 11.6 L16 7.8" fill="none" stroke="var(--green)" stroke-width="1.4"/>
        </svg>
        info@copperwrenbuilds.com
      </p>
      <span class="divider"></span>
      <p class="contact">
        <svg viewBox="0 0 22 22" aria-hidden="true">
          <circle cx="11" cy="11" r="10" fill="none" stroke="var(--green)" stroke-width="1.5"/>
          <circle cx="11" cy="11" r="5.5" fill="none" stroke="var(--green)" stroke-width="1.3"/>
          <ellipse cx="11" cy="11" rx="2.4" ry="5.5" fill="none" stroke="var(--green)" stroke-width="1.1"/>
          <path d="M5.5 11 H16.5" stroke="var(--green)" stroke-width="1.1"/>
        </svg>
        www.copperwrenbuilds.com
      </p>
    </div>
  </section>
</main>
</body>
</html>
```